Australian Dairy Business Requires Packaging Concept

We are an Australian Dairy Products Supplier exporting our goods predominantly to China including Baby Formula/Long Life Milk and Full Cream Milk Powder. We are looking for only conceptual art at this stage so we can synchronise with the most suitable designer.

The range incorporates the following and we have nicknamed the brand "Pelko" while in concept

1. "Pelko" Infant Formula Pack

Artwork is common but 3 colours in range are needed to denote 0-6months /6 -12 Months /1 Year olds + ( I have attached a crude mock up to assist in the explanantion and dont worry too much about the text its more the style of the design
We need key factors such as an illustrative Kangaroo and an illustrative Map of Australia - The size of each illustration does not matter let your creative skills dictate the best proportions. The Mock up brand name can be called "Pelko".

2. "Pelko" 1KG Full Cream Milk Powder

The artwork here is for 1 variety only with the look and style to be very similar to the Infant Formula however instead of a Kangaroo we would like an illustrative cow light brown in colour and again a illustrative map of Australia.I have attached a picture of the size of the box and the text is not in important at this stage just the concept within the range.

3. Pelko" 1 Litre Long Life MilkPelko

The artwork here is for 1 variety only with the look and style to be almost identical to the Full Cream Milk Powder.I have attached a picture of a typical sized long lide box box and the text is not important at this stage just the concept within the range.

Target Market(s)

Infant Formual Packs - Asian Parents who trust imported
goods from Australia

Milk Powder - Broad Chinese Demographic but consumer
based towards 25-60 yr old women

Milk Long Life - Broad Chiense Demographic consumer based with more equal spread of men and women 25-60yr old

Industry/Entity Type

Business

Requirements
Must have
• Infant Formual Packs can be fun in design but still professional so that marketing campaign can reinforce in future as a trusted brand and product.
Nice to have
• Range of products need to look like a family although subtle difference are welcom. At this stage we just want to seek out a concept.

```html
<!DOCTYPE html>
<html lang="en">
<head>
<meta charset="utf-8">
<title>Pelko Milk Powder Packaging Dielines</title>
<link href="https://fonts.googleapis.com/css2?family=Anton&family=Roboto+Condensed:wght@400;700&display=swap" rel="stylesheet">
<style>
  :root {
    --cyan: #3fc6ee;
    --cyan-pale: #86e2f7;
    --navy: #1d4d9e;
    --navy-deep: #163a7a;
    --white: #ffffff;
    --magenta: #e637c8;
    --frame: #c9d2d6;
    --panel-pale: #d8f3fb;
    --ink: #1b2b55;
  }
  * { box-sizing: border-box; margin: 0; padding: 0; }
  html, body { width: 828px; height: 1200px; overflow: hidden; background: var(--white); }
  body { position: relative; font-family: "Roboto Condensed", Arial, sans-serif; color: var(--white); }

  .dieline { position: absolute; left: 0; width: 828px; height: 590px; }
  .dieline--powder-full { top: 0; }
  .dieline--powder-plain { top: 615px; }

  .crop-label { position: absolute; color: var(--magenta); font-size: 6px; text-align: center; line-height: 1.1; }
  .crop-label--total { left: 370px; top: 2px; width: 60px; }
  .crop-rule { position: absolute; left: 20px; top: 21px; width: 750px; height: 0; border-top: 0.6px solid var(--magenta); }
  .column-labels { position: absolute; left: 0; top: 24px; width: 828px; height: 18px; }
  .column-labels span { position: absolute; color: var(--magenta); font-size: 6px; text-align: center; line-height: 1.2; }

  .frame { position: absolute; left: 20px; top: 44px; width: 752px; height: 524px; background: var(--frame); }
  .artwork { position: absolute; left: 30px; top: 48px; width: 732px; height: 508px; overflow: hidden; background: var(--cyan); }
  .artwork svg.waves { position: absolute; left: 0; top: 0; }

  .fin-note { position: absolute; color: var(--magenta); font-size: 9px; line-height: 10px; transform: rotate(-90deg); transform-origin: left top; white-space: nowrap; }
  .fin-note--seal { left: 32px; top: 335px; }
  .fin-note--hidden { left: 45px; top: 472px; }
  .margin-note { position: absolute; color: var(--magenta); font-size: 5.5px; transform: rotate(90deg); transform-origin: left top; white-space: nowrap; }

  .brand { position: absolute; left: 275px; top: 105px; width: 160px; text-align: center; }
  .brand-name { font-family: "Anton", Impact, sans-serif; font-size: 66px; line-height: 1; letter-spacing: 1px; color: var(--white); }
  .brand-sub { font-family: "Anton", Impact, sans-serif; font-size: 11px; margin-top: 2px; letter-spacing: .3px; }
  .brand-sub--plain { font-size: 13px; }
  .weight { position: absolute; left: 456px; top: 104px; font-family: "Anton", Impact, sans-serif; font-size: 13px; }
  .makes-badge { position: absolute; left: 432px; top: 136px; width: 50px; height: 50px; border-radius: 50%; background: var(--navy); border: 3px solid var(--white); text-align: center; font-weight: 700; line-height: 1; padding-top: 8px; }
  .makes-badge .small { font-size: 6px; }
  .makes-badge .big { font-size: 18px; }

  .illustration { position: absolute; left: 325px; top: 190px; width: 155px; height: 155px; border-radius: 30% 40% 35% 25%; }
  .illustration--kangaroo { background: radial-gradient(circle at 45% 55%, #e8a23c 0 30%, #ffffff 58%); }
  .illustration--cow { background: radial-gradient(circle at 40% 60%, #9a5a36 0 26%, #f2c6d6 36%, #ffffff 58%); }

  .text-block { position: absolute; font-size: 4.6px; line-height: 1.35; }
  .text-block h3 { font-size: 8px; font-weight: 700; margin-bottom: 3px; }
  .text-block h3 small { font-size: 4.5px; font-weight: 400; }
  .text-block h4 { font-size: 5px; font-weight: 700; margin: 3px 0 1px; }
  .recipe { left: 40px; top: 220px; width: 120px; }
  .directions { left: 160px; top: 160px; width: 105px; }
  .directions .cup-icon { display: block; width: 30px; height: 12px; margin: 3px 0; }

  .nutrition { position: absolute; left: 508px; top: 162px; width: 88px; height: 80px; background: var(--panel-pale); color: var(--ink); font-size: 3.6px; padding: 2px 3px; border: 1px solid var(--white); }
  .nutrition h4 { text-align: center; font-size: 4.6px; color: var(--navy); }
  .nutrition table { width: 100%; border-collapse: collapse; }
  .nutrition td { border-bottom: 0.4px solid #8ab6d8; padding: 0.4px 0; }
  .energy-box { position: absolute; left: 508px; top: 244px; width: 88px; height: 60px; background: var(--panel-pale); color: var(--ink); font-size: 3.8px; border: 1px solid var(--white); }
  .energy-box .title { background: var(--navy); color: var(--white); font-size: 4.6px; padding: 1px 3px; }
  .energy-ring { position: absolute; left: 3px; top: 13px; width: 30px; height: 30px; border-radius: 50%; border: 3px solid var(--navy); background: var(--white); text-align: center; font-size: 4.5px; font-weight: 700; color: var(--navy); padding-top: 5px; }
  .energy-box .note { position: absolute; left: 37px; top: 12px; width: 48px; line-height: 1.3; }
  .cert-marks { position: absolute; left: 510px; top: 310px; width: 70px; height: 22px; }
  .cert-marks span { display: inline-block; width: 16px; height: 16px; background: var(--navy-deep); margin-right: 18px; }

  .claims { position: absolute; left: 618px; top: 222px; width: 110px; }
  .claims li { list-style: none; font-size: 7.6px; font-weight: 700; line-height: 1.05; margin-bottom: 4px; padding-left: 10px; position: relative; }
  .claims li::before { content: ""; position: absolute; left: 0; top: 1px; width: 6px; height: 6px; border-radius: 50%; background: var(--cyan-pale); }
  .veg { position: absolute; left: 618px; top: 282px; font-size: 5.5px; font-style: italic; font-weight: 700; }
  .pack-info { position: absolute; left: 618px; top: 292px; width: 112px; font-size: 4.4px; line-height: 1.4; }

  .daily-strip { position: absolute; left: 278px; top: 392px; width: 210px; }
  .daily-strip .dots { display: flex; gap: 4px; }
  .daily-strip .dot { width: 28px; height: 28px; border-radius: 50%; background: var(--white); border: 2px solid var(--navy); color: var(--navy); font-size: 3.8px; font-weight: 700; text-align: center; padding-top: 6px; line-height: 1.2; }
  .daily-strip p { font-size: 3.8px; margin-top: 2px; }
</style>
</head>
<body>

<section class="dieline dieline--powder-full">
  <div class="crop-label crop-label--total">TOTAL CROP AREA<br>465mm</div>
  <div class="crop-rule"></div>
  <div class="column-labels">
    <span style="left:0;width:40px">FIN SEAL<br>10mm 10mm</span>
    <span style="left:70px;width:60px">BACK – RIGHT<br>75mm</span>
    <span style="left:200px;width:50px">SIDE<br>62.5mm</span>
    <span style="left:390px;width:60px">FRONT<br>160mm</span>
    <span style="left:555px;width:50px">SIDE<br>62.5mm</span>
    <span style="left:670px;width:60px">BACK – LEFT<br>75mm</span>
    <span style="left:745px;width:40px">FIN SEAL<br>10mm</span>
  </div>
  <div class="frame"></div>
  <div class="artwork">
    <svg class="waves" width="732" height="508" viewBox="0 0 732 508" aria-hidden="true">
      <rect width="732" height="508" fill="var(--cyan)"/>
      <path d="M0 10 H732 V70 C560 40 330 150 0 235 Z" fill="var(--navy)"/>
      <path d="M0 235 C330 150 560 40 732 70 V95 C560 80 330 185 0 262 Z" fill="var(--cyan-pale)"/>
      <path d="M0 470 C220 500 420 420 600 310 C650 280 700 230 732 190 V508 H0 Z" fill="var(--navy)"/>
      <path d="M0 455 C220 488 420 405 600 298 C650 268 700 220 732 175 V190 C700 230 650 280 600 310 C420 420 220 500 0 470 Z" fill="var(--cyan-pale)"/>
      <rect x="0" y="0" width="732" height="10" fill="var(--navy-deep)"/>
      <rect x="0" y="494" width="732" height="14" fill="var(--navy-deep)"/>
      <rect x="0" y="2" width="8" height="6" fill="#000"/>
      <rect x="0" y="497" width="8" height="6" fill="#000"/>
    </svg>
    <div class="brand"><div class="brand-name">Pelko</div><div class="brand-sub">Full Cream Milk Powder</div></div>
    <div class="weight">1kg</div>
    <div class="makes-badge"><div class="small">MAKES</div><div class="big">7</div><div class="small">LITRES</div></div>
    <div class="illustration illustration--kangaroo" role="img" aria-label="Illustrated kangaroo lounging over a white map of Australia"></div>

    <div class="text-block recipe">
      <h3>Mixed Berry Muffins <small>(Makes 12)</small></h3>
      <h4>Ingredients:</h4>
      2 cups self-raising flour<br>¼ cup caster sugar<br>1 cup reconstituted BROOKVALE® Full Cream Milk Powder<br>2 cups fresh mixed berries<br>2 eggs<br>1 teaspoon vanilla extract<br>100g butter, (melted)
      <h4>Method:</h4>
      1. Preheat oven to 180°C. Grease a 12 cup muffin pan or insert paper cups into pan.<br>2. Sift flour &amp; caster sugar into a bowl.<br>3. Whisk reconstituted BROOKVALE® Full Cream Milk Powder, eggs, vanilla and melted butter in a separate bowl until well combined.<br>4. Using spoon, stir wet mixture into dry ingredients, then fold in mixed berries without over mixing.<br>5. Spoon mixture into muffin pan and bake for 20–25 minutes.<br>6. Let muffins stand in pan for 5 minutes and transfer to a wire rack for cooling. Lightly dust with icing sugar if desired.<br>7. Serve with a tall glass of reconstituted BROOKVALE® Full Cream Milk Powder and Enjoy!
    </div>

    <div class="text-block directions">
      <h4>Directions for use:</h4>
      To make 1 litre:<br>1. Add 1½ cups (140g) of instant BROOKVALE® Full Cream Milk Powder to 3 cups of hot or cold water.<br>2. Stir until dissolved.<br>3. Add more water to make up 1 litre.
      <svg class="cup-icon" viewBox="0 0 30 12" aria-hidden="true"><rect x="1" y="3" width="7" height="8" fill="#fff"/><rect x="12" y="5" width="6" height="6" fill="#fff"/><rect x="22" y="2" width="7" height="9" fill="#fff"/></svg>
      To make 1 cup:<br>1. Add 2 tbsp (20g) of instant BROOKVALE® Full Cream Milk Powder to ¾ cup of hot or cold water.<br>2. Stir until dissolved.<br>3. Add more water to make up 1 cup.
      <h4>For best results always add powder to water.</h4>
      For richer flavour and extra nourishment, use additional powder to suit your personal taste or preference. To enhance the natural flavour of this product we recommend storing the reconstituted liquid milk in the refrigerator overnight prior to consumption.
    </div>

    <div class="nutrition">
      <h4>NUTRITION INFORMATION</h4>
      <div>Servings per package: 28 · Serving size: 250mL</div>
      <table>
        <tr><td>Energy</td><td>710kJ</td><td>8%</td><td>284kJ</td></tr>
        <tr><td>Protein</td><td>8.4g</td><td>17%</td><td>3.4g</td></tr>
        <tr><td>Fat, total</td><td>9.2g</td><td>13%</td><td>3.7g</td></tr>
        <tr><td>– saturated</td><td>6.0g</td><td>25%</td><td>2.4g</td></tr>
        <tr><td>Carbohydrate</td><td>12.5g</td><td>4%</td><td>5.0g</td></tr>
        <tr><td>– sugars</td><td>12.5g</td><td>14%</td><td>5.0g</td></tr>
        <tr><td>Sodium</td><td>100mg</td><td>4%</td><td>40mg</td></tr>
        <tr><td>Calcium</td><td>300mg</td><td>38%</td><td>120mg</td></tr>
      </table>
    </div>
    <div class="energy-box">
      <div class="title">(%DI) per 250mL serve</div>
      <div class="energy-ring">Energy<br>8%<br>710kJ</div>
      <div class="note">% Daily Intake based on an average adult diet of 8700kJ. Your daily intakes may be higher or lower depending on your energy needs.</div>
    </div>
    <div class="cert-marks" aria-hidden="true"><span></span><span></span></div>

    <ul class="claims">
      <li>Naturally a Good Source of Calcium</li>
      <li>Naturally a Source of Protein</li>
      <li>No Preservatives</li>
    </ul>
    <div class="veg">✓ Suitable for vegetarians</div>
    <div class="pack-info">
      <b>Ingredients:</b> Full Cream Milk, Emulsifier (322 From Soy).<br>
      Store in a cool, dry place. After reconstitution, store refrigerated below 4°C and consume within 3 days.<br>
      Product of Australia.<br>
      Specially made for Harbour Stores by our suppliers to strict quality standards. If you are not satisfied with this product, please return it to your nearest store for a full refund or replacement.<br>
      HARBOUR STORES<br>PO BOX 100<br>EASTBROOK NSW 2999<br>www.harbourstores.example<br>
      BROOKVALE® is a registered trademark of Harbour Stores.
    </div>

    <div class="daily-strip">
      <div class="dots">
        <div class="dot">Energy<br>8%<br>710kJ</div>
        <div class="dot">Fat<br>13%<br>9.2g</div>
        <div class="dot">Sat Fat<br>25%<br>6.0g</div>
        <div class="dot">Sugar<br>15%<br>12.5g</div>
        <div class="dot">Sodium<br>5%<br>100mg</div>
        <div class="dot">Calcium<br>38%<br>300mg</div>
      </div>
      <p>% Daily Intake (%DI) per 250mL serve<br>% Recommended Dietary Intake (%RDI) per 250mL serve</p>
    </div>
  </div>
  <div class="fin-note fin-note--seal">FIN SEAL</div>
  <div class="fin-note fin-note--hidden">HIDDEN BY FOLDED FIN SEAL</div>
  <div class="margin-note" style="left:790px;top:60px">TOP 10 · 31.25mm</div>
  <div class="margin-note" style="left:790px;top:265px">222.5mm</div>
  <div class="margin-note" style="left:805px;top:255px">TOTAL CROP AREA 315mm</div>
  <div class="margin-note" style="left:790px;top:500px">BOTTOM 31.25mm · 10</div>
</section>

<section class="dieline dieline--powder-plain">
  <div class="crop-label crop-label--total">TOTAL CROP AREA<br>465mm</div>
  <div class="crop-rule"></div>
  <div class="column-labels">
    <span style="left:0;width:40px">FIN SEAL<br>10mm 10mm</span>
    <span style="left:70px;width:60px">BACK – RIGHT<br>75mm</span>
    <span style="left:200px;width:50px">SIDE<br>62.5mm</span>
    <span style="left:390px;width:60px">FRONT<br>160mm</span>
    <span style="left:555px;width:50px">SIDE<br>62.5mm</span>
    <span style="left:670px;width:60px">BACK – LEFT<br>75mm</span>
    <span style="left:745px;width:40px">FIN SEAL<br>10mm</span>
  </div>
  <div class="frame"></div>
  <div class="artwork">
    <svg class="waves" width="732" height="508" viewBox="0 0 732 508" aria-hidden="true">
      <rect width="732" height="508" fill="var(--cyan)"/>
      <path d="M0 10 H732 V70 C560 40 330 150 0 235 Z" fill="var(--navy)"/>
      <path d="M0 235 C330 150 560 40 732 70 V95 C560 80 330 185 0 262 Z" fill="var(--cyan-pale)"/>
      <path d="M0 470 C220 500 420 420 600 310 C650 280 700 230 732 190 V508 H0 Z" fill="var(--navy)"/>
      <path d="M0 455 C220 488 420 405 600 298 C650 268 700 220 732 175 V190 C700 230 650 280 600 310 C420 420 220 500 0 470 Z" fill="var(--cyan-pale)"/>
      <rect x="0" y="0" width="732" height="10" fill="var(--navy-deep)"/>
      <rect x="0" y="494" width="732" height="14" fill="var(--navy-deep)"/>
      <rect x="0" y="2" width="8" height="6" fill="#000"/>
      <rect x="0" y="497" width="8" height="6" fill="#000"/>
    </svg>
    <div class="brand"><div class="brand-name">Pelko</div><div class="brand-sub brand-sub--plain">MILK POWDER</div></div>
    <div class="weight">1kg</div>
    <div class="makes-badge"><div class="small">MAKES</div><div class="big">7</div><div class="small">LITRES</div></div>
    <div class="illustration illustration--cow" role="img" aria-label="Illustrated light brown cow with a bell standing over a white map of Australia"></div>

    <div class="text-block recipe">
      <h3>Mixed Berry Muffins <small>(Makes 12)</small></h3>
      <h4>Ingredients:</h4>
      2 cups self-raising flour<br>¼ cup caster sugar<br>1 cup reconstituted BROOKVALE® Full Cream Milk Powder<br>2 cups fresh mixed berries<br>2 eggs<br>1 teaspoon vanilla extract<br>100g butter, (melted)
      <h4>Method:</h4>
      1. Preheat oven to 180°C. Grease a 12 cup muffin pan or insert paper cups into pan.<br>2. Sift flour &amp; caster sugar into a bowl.<br>3. Whisk reconstituted BROOKVALE® Full Cream Milk Powder, eggs, vanilla and melted butter in a separate bowl until well combined.<br>4. Using spoon, stir wet mixture into dry ingredients, then fold in mixed berries without over mixing.<br>5. Spoon mixture into muffin pan and bake for 20–25 minutes.<br>6. Let muffins stand in pan for 5 minutes and transfer to a wire rack for cooling. Lightly dust with icing sugar if desired.<br>7. Serve with a tall glass of reconstituted BROOKVALE® Full Cream Milk Powder and Enjoy!
    </div>

    <div class="text-block directions">
      <h4>Directions for use:</h4>
      To make 1 litre:<br>1. Add 1½ cups (140g) of instant BROOKVALE® Full Cream Milk Powder to 3 cups of hot or cold water.<br>2. Stir until dissolved.<br>3. Add more water to make up 1 litre.
      <svg class="cup-icon" viewBox="0 0 30 12" aria-hidden="true"><rect x="1" y="3" width="7" height="8" fill="#fff"/><rect x="12" y="5" width="6" height="6" fill="#fff"/><rect x="22" y="2" width="7" height="9" fill="#fff"/></svg>
      To make 1 cup:<br>1. Add 2 tbsp (20g) of instant BROOKVALE® Full Cream Milk Powder to ¾ cup of hot or cold water.<br>2. Stir until dissolved.<br>3. Add more water to make up 1 cup.
      <h4>For best results always add powder to water.</h4>
      For richer flavour and extra nourishment, use additional powder to suit your personal taste or preference. To enhance the natural flavour of this product we recommend storing the reconstituted liquid milk in the refrigerator overnight prior to consumption.
    </div>

    <div class="nutrition">
      <h4>NUTRITION INFORMATION</h4>
      <div>Servings per package: 28 · Serving size: 250mL</div>
      <table>
        <tr><td>Energy</td><td>710kJ</td><td>8%</td><td>284kJ</td></tr>
        <tr><td>Protein</td><td>8.4g</td><td>17%</td><td>3.4g</td></tr>
        <tr><td>Fat, total</td><td>9.2g</td><td>13%</td><td>3.7g</td></tr>
        <tr><td>– saturated</td><td>6.0g</td><td>25%</td><td>2.4g</td></tr>
        <tr><td>Carbohydrate</td><td>12.5g</td><td>4%</td><td>5.0g</td></tr>
        <tr><td>– sugars</td><td>12.5g</td><td>14%</td><td>5.0g</td></tr>
        <tr><td>Sodium</td><td>100mg</td><td>4%</td><td>40mg</td></tr>
        <tr><td>Calcium</td><td>300mg</td><td>38%</td><td>120mg</td></tr>
      </table>
    </div>
    <div class="energy-box">
      <div class="title">(%DI) per 250mL serve</div>
      <div class="energy-ring">Energy<br>8%<br>710kJ</div>
      <div class="note">% Daily Intake based on an average adult diet of 8700kJ. Your daily intakes may be higher or lower depending on your energy needs.</div>
    </div>
    <div class="cert-marks" aria-hidden="true"><span></span><span></span></div>

    <ul class="claims">
      <li>Naturally a Good Source of Calcium</li>
      <li>Naturally a Source of Protein</li>
      <li>No Preservatives</li>
    </ul>
    <div class="veg">✓ Suitable for vegetarians</div>
    <div class="pack-info">
      <b>Ingredients:</b> Full Cream Milk, Emulsifier (322 From Soy).<br>
      Store in a cool, dry place. After reconstitution, store refrigerated below 4°C and consume within 3 days.<br>
      Product of Australia.<br>
      Specially made for Harbour Stores by our suppliers to strict quality standards. If you are not satisfied with this product, please return it to your nearest store for a full refund or replacement.<br>
      HARBOUR STORES<br>PO BOX 100<br>EASTBROOK NSW 2999<br>www.harbourstores.example<br>
      BROOKVALE® is a registered trademark of Harbour Stores.
    </div>

    <div class="daily-strip">
      <div class="dots">
        <div class="dot">Energy<br>8%<br>710kJ</div>
        <div class="dot">Fat<br>13%<br>9.2g</div>
        <div class="dot">Sat Fat<br>25%<br>6.0g</div>
        <div class="dot">Sugar<br>15%<br>12.5g</div>
        <div class="dot">Sodium<br>5%<br>100mg</div>
        <div class="dot">Calcium<br>38%<br>300mg</div>
      </div>
      <p>% Daily Intake (%DI) per 250mL serve<br>% Recommended Dietary Intake (%RDI) per 250mL serve</p>
    </div>
  </div>
  <div class="fin-note fin-note--seal">FIN SEAL</div>
  <div class="fin-note fin-note--hidden">HIDDEN BY FOLDED FIN SEAL</div>
  <div class="margin-note" style="left:790px;top:60px">TOP 10 · 31.25mm</div>
  <div class="margin-note" style="left:790px;top:265px">222.5mm</div>
  <div class="margin-note" style="left:805px;top:255px">TOTAL CROP AREA 315mm</div>
  <div class="margin-note" style="left:790px;top:500px">BOTTOM 31.25mm · 10</div>
</section>

</body>
</html>
```